Corporate Powerpoint Presentation Template

Ru Tambisk Technology Consulting Group is looking to have a comprehensive Powerpoint Template designed. The template must contain a wide selection for slide templates that can be used for proposals, project reporting and general marketing purposes, including graphs, infographics etc.. Please review supporting documentation attached.

```html
<!DOCTYPE html>
<html lang="en">
<head>
<meta charset="utf-8">
<title>Ru Tambisk Technology Consulting Group — Presentation Template</title>
<link href="https://fonts.googleapis.com/css2?family=Poppins:ital,wght@0,400;0,500;0,600;0,700;1,400&display=swap" rel="stylesheet">
<style>
:root{
  --navy:#17137a;
  --navy-2:#2a2a9a;
  --gold:#d2b06a;
  --gold-soft:#e9d9b4;
  --lav:#b9b3dc;
  --page:#d8d8d6;
  --slide:#f3f3f3;
  --card:#ffffff;
  --ink:#26263a;
  --muted:#7a7a86;
  --line:#e2e2e6;
}
*{box-sizing:border-box;margin:0;padding:0}
html,body{width:1200px;height:3260px;overflow:hidden}
body{background:var(--page);font-family:"Poppins",sans-serif;color:var(--ink);position:relative}
.slide{position:absolute;width:542px;height:304px;background:var(--slide);overflow:hidden}
.abs{position:absolute}
.ttl{position:absolute;font-weight:600;font-size:22px;line-height:1.12;color:var(--navy)}
.gold{color:var(--gold)}
.navy{color:var(--navy)}
.txt{font-size:6px;line-height:1.45;color:var(--muted)}
.txt b{color:var(--ink);font-weight:600}
.foot{position:absolute;left:36px;bottom:20px;font-size:6px;color:var(--muted)}
.foot b{color:var(--navy);font-weight:600;margin-right:6px}
.pg{position:absolute;right:36px;bottom:20px;font-size:7px;font-weight:600;color:var(--navy)}
.card{position:absolute;background:var(--card);border-radius:4px;box-shadow:0 1px 4px rgba(20,20,60,.08)}
.chk{display:inline-flex;width:11px;height:11px;border-radius:50%;border:1px solid var(--gold);color:var(--navy);font-size:6px;font-style:normal;align-items:center;justify-content:center;flex:none}
.num{display:inline-flex;width:11px;height:11px;border-radius:50%;border:1px solid var(--gold);color:var(--navy);font-size:5.5px;align-items:center;justify-content:center;flex:none;font-weight:600}
.row{display:flex;gap:6px;align-items:flex-start}
.photo{position:absolute}
.icon{width:12px;height:12px;display:block;margin-bottom:6px}

/* cover */
.cover{background:linear-gradient(120deg,#3a3aa6 0%,#5b52c4 45%,#9a6bd9 100%)}
.cover .nav{position:absolute;top:30px;right:32px;display:flex;gap:22px;font-size:7px;color:#fff}
.cover .nav span{text-decoration:underline}
.brand{font-weight:700;font-size:14px;color:var(--gold);letter-spacing:.5px}
/* pricing */
.plan{position:absolute;top:58px;width:100px;height:202px;background:var(--card);border-radius:4px;box-shadow:0 1px 4px rgba(20,20,60,.08);overflow:hidden}
.plan .hd{height:62px;padding:10px 9px;color:#fff}
.plan .hd p{font-size:6.5px;font-weight:500}
.plan .hd strong{display:block;font-size:20px;font-weight:600;margin-top:4px}
.plan .hd strong small{font-size:9px;margin-left:3px}
.plan ul{list-style:none;padding:10px 12px;font-size:5.6px;line-height:1.6;color:var(--muted)}
.plan ul li:before{content:"• "}
.plan .btn{position:absolute;left:8px;right:8px;bottom:8px;height:20px;border-radius:3px;color:#fff;font-size:6px;font-weight:600;display:flex;align-items:center;justify-content:center}
.bg-navy{background:var(--navy)}
.bg-gold{background:var(--gold)}
/* compare table */
.cmp{position:absolute;left:34px;top:40px;width:476px;border-collapse:collapse;font-size:5.6px;table-layout:fixed}
.cmp th{background:var(--navy);color:#fff;font-weight:600;height:12px}
.cmp td{height:15.8px;border-bottom:1px solid var(--line);text-align:center;color:var(--navy)}
.cmp td:first-child{text-align:left;color:var(--ink)}
.cmp tr.price td{font-weight:600;background:#e6e6ea}
.cmp td.hl,.cmp th.hl{background:#fff}
.cmp th.hl{background:var(--gold)}
.cmp tr.price td.hl{background:var(--navy);color:#fff}
/* steps */
.step{position:absolute;width:152px;display:flex;gap:8px}
.step .no{flex:none;width:26px;height:26px;border:1px solid var(--line);background:#fff;border-radius:3px;font-size:7px;font-weight:600;color:var(--navy);display:flex;align-items:center;justify-content:center}
.rm{position:absolute;width:232px;height:44px;display:flex;gap:8px;align-items:center;background:#fff;border-radius:4px;padding:4px}
.rm .bd{flex:none;width:50px;height:36px;border-radius:3px;color:#fff;font-size:6px;font-weight:600;display:flex;align-items:center;justify-content:center;text-align:center;line-height:1.2}
.rm .ring{position:absolute;right:4px;top:4px;width:9px;height:9px;border-radius:50%;border:1px solid var(--navy)}
.tabs{position:absolute;left:36px;top:18px;width:472px;height:24px;background:#fff;border-radius:4px;display:flex;justify-content:center;gap:18px;align-items:center;font-size:5.8px;color:var(--navy);font-weight:500}
.tabs .on{border-top:2px solid var(--gold);padding-top:4px;margin-top:-6px}
</style>
</head>
<body>

<!-- 1 Cover -->
<section class="slide cover" style="left:61px;top:61px" role="img" aria-label="Cover slide over a violet glowing technology circuit background">
  <div class="abs" style="left:225px;top:0;width:34px;height:5px;background:var(--gold)"></div>
  <div class="nav"><span>Home</span><span>About Us</span><span>Service</span><span>Report</span><span>Contact Us</span></div>
  <div class="abs brand" style="left:54px;top:78px">RT</div>
  <h1 class="abs" style="left:54px;top:122px;font-size:29px;font-weight:500;line-height:1.12;color:#fff">Introduction to<br>Ru Tambisk</h1>
  <p class="abs" style="left:54px;top:212px;font-size:7px;line-height:1.4;color:#fff">Empowering Enterprises to Innovate through<br>Intelligent Architecture, Automation &amp; AI</p>
  <p class="abs" style="left:54px;top:275px;font-size:6.5px;color:#fff">February 2026</p>
</section>

<!-- 2 Title -->
<section class="slide" style="left:615px;top:61px">
  <div class="abs" style="left:56px;top:50px;font-size:5.5px;line-height:1.4">Mar 20th, 2026<br><b>RT Studio</b></div>
  <div class="abs" style="left:250px;top:50px;font-size:5.5px;line-height:1.4;text-align:center">RT Studio<br><b>Presentation</b></div>
  <div class="abs" style="right:52px;top:50px;font-size:5.5px;line-height:1.4;text-align:right">Presented by<br><b>RT Studio</b></div>
  <h2 class="abs" style="left:0;right:0;top:120px;text-align:center;font-size:31px;font-weight:600;line-height:1.05;color:var(--navy)">Introduction to<br>Ru <span class="gold">Tambisk</span></h2>
  <p class="abs" style="left:0;right:0;top:210px;text-align:center;font-size:6.5px;letter-spacing:2px">February 2026</p>
  <p class="abs" style="left:0;right:0;top:250px;text-align:center;font-size:11px;font-weight:600;color:#9a9aa6">Ru Tambisk</p>
</section>

<!-- 3 About -->
<section class="slide" style="left:61px;top:376px">
  <div class="photo" style="left:0;top:0;width:542px;height:150px;background:linear-gradient(120deg,#1b2a6e,#3a5fb8 60%,#7fa3e6)" role="img" aria-label="Hand touching a glowing automation interface"></div>
  <div class="card" style="left:62px;top:137px;width:420px;height:150px;border-radius:0">
    <div class="abs" style="left:26px;top:34px;width:108px;height:16px;background:var(--navy);color:#fff;font-size:10px;display:flex;align-items:center;justify-content:center">About Us</div>
    <p class="abs" style="left:24px;top:68px;width:370px;font-size:7px;line-height:2;color:var(--ink)">At Ru Tambisk, we believe that technology should always enable and create value. Our mission is to empower our customers with seamless integration solutions and intelligent automation that transforms their operations and accelerates business growth.</p>
  </div>
</section>

<!-- 4 Essential elements -->
<section class="slide" style="left:615px;top:376px">
  <h2 class="ttl" style="left:36px;top:30px"><span class="gold">Essential Elements of</span><br><span class="gold">a Robust</span> Financial Plan</h2>
  <p class="abs txt" style="left:36px;top:98px;width:240px">A robust Financial Plan is your guide to achieving financial stability and growth. It should encompass these six crucial elements:</p>
  <div class="abs row" style="left:52px;top:150px;width:140px"><i class="num">1</i><p class="txt"><b>Income Management</b>: A thorough review of your income sources and tactics to enhance them.</p></div>
  <div class="abs row" style="left:200px;top:150px;width:140px"><i class="num">2</i><p class="txt"><b>Savings Strategy</b>: Plans for setting aside a portion of your income for future needs and emergencies.</p></div>
  <div class="abs row" style="left:350px;top:150px;width:140px"><i class="num">3</i><p class="txt"><b>Risk Management and Insurance</b>: Provisions to safeguard against unexpected financial risks.</p></div>
  <div class="abs row" style="left:52px;top:183px;width:140px"><i class="num">4</i><p class="txt"><b>Expense and Debt Management</b>: An examination of your spending patterns aimed at minimizing unnecessary expenses and a strategy to reduce and eliminate any existing debts.</p></div>
  <div class="abs row" style="left:200px;top:183px;width:140px"><i class="num">5</i><p class="txt"><b>Investment Planning</b>: Short-term and long-term investment strategies to grow your wealth.</p></div>
  <div class="abs row" style="left:350px;top:183px;width:140px"><i class="num">6</i><p class="txt"><b>Retirement and Estate Planning</b>: A long-term strategy to ensure a comfortable retirement and plans for the distribution of your assets after your lifetime.</p></div>
  <div class="foot"><b>RT</b>Introduction to Ru Tambisk</div><div class="pg">4</div>
</section>

<!-- 5 Agenda -->
<section class="slide" style="left:61px;top:690px">
  <h2 class="abs" style="left:48px;top:42px;font-size:31px;font-weight:500;color:var(--navy)">Agenda</h2>
  <ol class="abs" style="left:46px;top:120px;list-style:none;font-size:6.5px;line-height:25.5px">
    <li><span class="txt" style="margin-right:14px">01.</span><b>About Us</b></li>
    <li><span class="txt" style="margin-right:14px">02.</span><b>Speakers Introduction</b></li>
    <li><span class="txt" style="margin-right:14px">03.</span><b>Our Expertise</b></li>
    <li><span class="txt" style="margin-right:14px">04.</span><b>Break time</b></li>
    <li><span class="txt" style="margin-right:14px">05.</span><b>Speakers</b></li>
    <li><span class="txt" style="margin-right:14px">06.</span><b>Free time</b></li>
  </ol>
  <div class="photo" style="left:309px;top:0;width:233px;height:304px;background:linear-gradient(160deg,#5a5f6e,#2d2f3a 60%,#1a1b22)" role="img" aria-label="Team collaborating at a sticky-note wall in a modern office"></div>
  <div class="abs" style="left:482px;top:180px;width:60px;height:124px;background:var(--gold)">
    <svg class="abs" style="left:22px;bottom:14px" width="16" height="8" viewBox="0 0 16 8"><path d="M0 4h14M10 0l4 4-4 4" stroke="#fff" fill="none" stroke-width="1"/></svg>
  </div>
</section>

<!-- 6 Investment report -->
<section class="slide" style="left:615px;top:690px">
  <h2 class="ttl" style="left:36px;top:42px">Decoding an<br><span class="gold">Investment</span><br><span class="gold">Report</span>: 8 Key<br>Components</h2>
  <p class="abs txt" style="left:36px;top:152px;width:150px">An Investment Report is a comprehensive document that provides detailed information about your investment portfolio. It serves as a tool for tracking the performance of your investments, understanding the dynamics of the market, and making informed decisions about future investment strategies. By offering insights into the strengths and weaknesses of your portfolio, it plays a crucial role in shaping your investment approach. Here are the eight key components that an effective investment report should include:</p>
  <div class="card" style="left:200px;top:58px;width:146px;height:40px"></div>
  <div class="card" style="left:364px;top:58px;width:146px;height:40px"></div>
  <div class="abs row" style="left:206px;top:64px;width:138px"><i class="chk">✓</i><p class="txt"><b>Executive Summary</b>: A brief overview of the report's contents and the overall performance of the investment portfolio.</p></div>
  <div class="abs row" style="left:370px;top:64px;width:138px"><i class="chk">✓</i><p class="txt"><b>Asset Allocation</b>: A review of how assets are distributed across various investment categories and whether this aligns with the investor's risk tolerance and goals.</p></div>
  <div class="abs row" style="left:206px;top:116px;width:138px"><i class="chk">✓</i><p class="txt"><b>Portfolio Overview</b>: A detailed breakdown of the current portfolio, including the types of investments (stocks, bonds, real estate, etc.) and their respective proportions.</p></div>
  <div class="abs row" style="left:370px;top:116px;width:138px"><i class="chk">✓</i><p class="txt"><b>Market Commentary</b>: An analysis of current market conditions and how they impact the portfolio.</p></div>
  <div class="abs row" style="left:206px;top:166px;width:138px"><i class="chk">✓</i><p class="txt"><b>Performance Analysis</b>: An evaluation of the portfolio's performance over a specific period, compared to relevant benchmarks.</p></div>
  <div class="abs row" style="left:370px;top:166px;width:138px"><i class="chk">✓</i><p class="txt"><b>Recommendations</b>: Suggestions for improving the portfolio's performance, such as rebalancing strategies or new investment opportunities.</p></div>
  <div class="abs row" style="left:206px;top:214px;width:138px"><i class="chk">✓</i><p class="txt"><b>Risk Assessment</b>: An analysis of the portfolio's risk profile, considering factors like market volatility and investment diversification.</p></div>
  <div class="abs row" style="left:370px;top:214px;width:138px"><i class="chk">✓</i><p class="txt"><b>Future Outlook</b>: Projections for the portfolio's performance based on market trends and the investor's financial goals.</p></div>
  <div class="foot"><b>RT</b>Introduction to Ru Tambisk</div><div class="pg">6</div>
</section>

<!-- 7 Pricing -->
<section class="slide" style="left:61px;top:1009px">
  <h2 class="ttl" style="left:36px;top:20px">Pricing <span class="gold">Tables</span></h2>
  <div class="plan" style="left:36px"><div class="hd bg-navy"><p>Starter Plan</p><strong>25<small>$</small></strong></div>
    <ul><li>Financial Planning</li><li>Market Research</li><li>Risk Management</li><li>Marketing Strategy</li><li>IT Consulting Services</li><li>Human Resources</li><li>Mergers Guidance</li><li>Project Management</li><li>Corporate Training</li></ul><div class="btn bg-navy">More Info</div></div>
  <div class="plan" style="left:157px"><div class="hd bg-gold"><p>Growth Plan</p><strong>50<small>$</small></strong></div>
    <ul><li>Financial Planning</li><li>Market Research</li><li>Risk Management</li><li>Marketing Strategy</li><li>IT Consulting Services</li><li>Human Resources</li><li>Mergers Guidance</li><li>Project Management</li><li>Corporate Training</li></ul><div class="btn bg-gold">More Info</div></div>
  <div class="plan" style="left:278px"><div class="hd bg-navy"><p>Premium Plan</p><strong>99<small>$</small></strong></div>
    <ul><li>Financial Planning</li><li>Market Research</li><li>Risk Management</li><li>Marketing Strategy</li><li>IT Consulting Services</li><li>Human Resources</li><li>Mergers Guidance</li><li>Project Management</li><li>Corporate Training</li></ul><div class="btn bg-navy">More Info</div></div>
  <div class="plan" style="left:399px"><div class="hd bg-gold"><p>Enterprise Plan</p><strong>100<small>$</small></strong></div>
    <ul><li>Financial Planning</li><li>Market Research</li><li>Risk Management</li><li>Marketing Strategy</li><li>IT Consulting Services</li><li>Human Resources</li><li>Mergers Guidance</li><li>Project Management</li><li>Corporate Training</li></ul><div class="btn bg-gold">More Info</div></div>
  <div class="foot"><b>RT</b>Introduction to Ru Tambisk</div><div class="pg">7</div>
</section>

<!-- 8 Comparison -->
<section class="slide" style="left:615px;top:1009px">
  <div class="abs" style="left:305px;top:28px;width:64px;height:12px;background:var(--gold);border-radius:3px 3px 0 0"></div>
  <table class="cmp">
    <colgroup><col style="width:140px"><col><col><col><col><col></colgroup>
    <tr><th style="background:none"></th><th>Starter</th><th>Growth</th><th class="hl">Premium</th><th>Enterprise</th><th>Best</th></tr>
    <tr class="price"><td>Price</td><td>$2,500</td><td>$3,700</td><td class="hl">$6,600</td><td>$8,100</td><td>$15,000</td></tr>
    <tr><td>Business Strategy Consultation</td><td>✓</td><td>✓</td><td class="hl">✓</td><td>✓</td><td>✓</td></tr>
    <tr><td>Financial Planning Services</td><td>✓</td><td>✓</td><td class="hl">✓</td><td>✓</td><td>✓</td></tr>
    <tr><td>Market Research Analysis</td><td>✓</td><td>✓</td><td class="hl">✓</td><td>✓</td><td>✓</td></tr>
    <tr><td>Risk Management Assessment</td><td>✓</td><td>✓</td><td class="hl">✓</td><td>✓</td><td>✓</td></tr>
    <tr><td>Operational Efficiency Review</td><td>✓</td><td>✓</td><td class="hl">✓</td><td>✓</td><td>✓</td></tr>
    <tr><td>Branding and Marketing Strategy</td><td>✓</td><td>✓</td><td class="hl">✓</td><td>✓</td><td>✓</td></tr>
    <tr><td>IT Consulting Services</td><td>✓</td><td>✓</td><td class="hl">✓</td><td>✓</td><td>✓</td></tr>
    <tr><td>Human Resources Advisory</td><td></td><td>✓</td><td class="hl">✓</td><td>✓</td><td>✓</td></tr>
    <tr><td>Mergers and Acquisitions Guidance</td><td></td><td></td><td class="hl">✓</td><td>✓</td><td>✓</td></tr>
    <tr><td>Project Management Support</td><td></td><td></td><td class="hl">✓</td><td>✓</td><td>✓</td></tr>
    <tr><td>Regulatory Compliance Assistance</td><td></td><td></td><td class="hl"></td><td>✓</td><td>✓</td></tr>
    <tr><td>Customer Experience Optimization</td><td></td><td></td><td class="hl"></td><td></td><td>✓</td></tr>
  </table>
  <div class="foot"><b>RT</b>Introduction to Ru Tambisk</div><div class="pg">8</div>
</section>

<!-- 9 Testimonial -->
<section class="slide" style="left:61px;top:1325px">
  <h2 class="ttl" style="left:36px;top:30px">Transforming <span class="gold">Financial</span><br><span class="gold">Strategy</span> with Expert<br>Guidance</h2>
  <div class="photo" style="left:309px;top:0;width:233px;height:304px;background:linear-gradient(160deg,#b7a58c,#6d5a47 55%,#3a3029)" role="img" aria-label="Consultant and client reviewing documents at a meeting table"></div>
  <div class="card" style="left:36px;top:112px;width:290px;height:144px;border-radius:0">
    <div class="abs" style="left:14px;top:6px;font-size:30px;color:#d6d6dc;line-height:1">“</div>
    <p class="abs" style="left:26px;top:24px;width:248px;font-size:7px;font-style:italic;line-height:1.4;color:var(--muted)">The consulting agency's team transformed our financial strategy with their deep understanding of our needs. They crafted a plan that provided a clear roadmap for our future, enabling effective decision-making and resource optimization. Their professionalism and commitment were commendable. I highly recommend their services.</p>
    <div class="abs bg-navy" style="left:0;bottom:0;width:290px;height:38px;color:#fff;padding:10px 22px;font-size:7.5px;line-height:1.2">Mara Elwood<br><span style="font-size:5.5px">Chief Executive Officer</span></div>
  </div>
  <div class="pg" style="right:232px;color:#fff">9</div>
</section>

<!-- 10 Blueprint banner -->
<section class="slide" style="left:615px;top:1325px">
  <div class="photo" style="left:36px;top:28px;width:472px;height:132px;background:linear-gradient(110deg,#26268a,#3b4fae 50%,#5d86d4)" role="img" aria-label="Blue technology banner with a hand on an automation interface"></div>
  <h2 class="abs" style="left:56px;top:44px;font-size:20px;font-weight:500;line-height:1.15;color:#fff">Financial Blueprint for<br>Future Growth</h2>
  <p class="abs" style="left:56px;top:100px;width:240px;font-size:6px;line-height:1.45;color:#fff">This project involved the development of a comprehensive financial plan for a rapidly growing tech company. The plan was designed to support the company's ambitious growth objectives while ensuring financial stability and sustainability.</p>
  <div class="card" style="left:36px;top:174px;width:146px;height:86px;padding:12px"><svg class="icon" viewBox="0 0 12 12"><circle cx="6" cy="6" r="5" fill="none" stroke="var(--navy)" stroke-width="1.4"/><circle cx="6" cy="6" r="2" fill="var(--navy)"/></svg><p class="txt"><b>Complexity</b>: The project demanded a deep understanding of the unique financial aspects of the tech industry.</p></div>
  <div class="card" style="left:198px;top:174px;width:146px;height:86px;padding:12px"><svg class="icon" viewBox="0 0 12 12"><circle cx="4" cy="8" r="3" fill="none" stroke="var(--gold)" stroke-width="1.4"/><circle cx="9" cy="3.5" r="2.4" fill="none" stroke="var(--gold)" stroke-width="1.4"/></svg><p class="txt"><b>Impact</b>: The developed financial plan significantly shaped the client's business strategy and success.</p></div>
  <div class="card" style="left:362px;top:174px;width:146px;height:86px;padding:12px"><svg class="icon" viewBox="0 0 12 12"><path d="M4 1h4M5 1v4L1 11h10L7 5V1" fill="var(--navy)"/></svg><p class="txt"><b>Innovation</b>: Balancing aggressive growth with financial prudence required innovative thinking.</p></div>
  <div class="pg">10</div>
</section>

<!-- 11 Blueprint card -->
<section class="slide" style="left:61px;top:1643px">
  <div class="photo" style="left:36px;top:38px;width:300px;height:218px;border-radius:4px;background:linear-gradient(130deg,#29268e,#5c56b8 55%,#a7a3d6)" role="img" aria-label="Person working at a desk, tinted violet"></div>
  <h2 class="abs" style="left:62px;top:88px;font-size:20px;font-weight:500;line-height:1.2;color:#fff">Financial<br>Blueprint for<br>Future Growth</h2>
  <p class="abs" style="left:62px;top:185px;width:150px;font-size:5.8px;line-height:1.45;color:#fff">This project involved the development of a comprehensive financial plan for a rapidly growing tech company. The plan was designed to support the company's ambitious growth objectives while ensuring financial stability and sustainability.</p>
  <div class="card" style="left:350px;top:38px;width:156px;height:62px;padding:10px"><svg class="icon" viewBox="0 0 12 12"><circle cx="6" cy="6" r="5" fill="none" stroke="var(--navy)" stroke-width="1.4"/><circle cx="6" cy="6" r="2" fill="var(--navy)"/></svg><p class="txt"><b>Complexity</b>: The project demanded a deep understanding of the unique financial aspects of the tech industry.</p></div>
  <div class="card" style="left:350px;top:116px;width:156px;height:62px;padding:10px"><svg class="icon" viewBox="0 0 12 12"><circle cx="4" cy="8" r="3" fill="none" stroke="var(--gold)" stroke-width="1.4"/><circle cx="9" cy="3.5" r="2.4" fill="none" stroke="var(--gold)" stroke-width="1.4"/></svg><p class="txt"><b>Impact</b>: The developed financial plan significantly shaped the client's business strategy and success.</p></div>
  <div class="card" style="left:350px;top:194px;width:156px;height:62px;padding:10px"><svg class="icon" viewBox="0 0 12 12"><path d="M4 1h4M5 1v4L1 11h10L7 5V1" fill="var(--navy)"/></svg><p class="txt"><b>Innovation</b>: Balancing aggressive growth with financial prudence required innovative thinking.</p></div>
  <div class="pg">11</div>
</section>

<!-- 12 Blueprint list -->
<section class="slide" style="left:615px;top:1643px">
  <h2 class="ttl" style="left:36px;top:30px">Financial <span class="gold">Blueprint</span><br>for Future Growth</h2>
  <p class="abs txt" style="left:285px;top:48px;width:220px">This project involved the development of a comprehensive financial plan for a rapidly growing tech company. The plan was designed to support the company's ambitious growth objectives while ensuring financial stability and sustainability.</p>
  <div class="card" style="left:36px;top:100px;width:230px;height:166px"></div>
  <div class="abs" style="left:36px;top:155px;width:230px;border-top:1px solid var(--line)"></div>
  <div class="abs" style="left:36px;top:210px;width:230px;border-top:1px solid var(--line)"></div>
  <div class="abs row" style="left:46px;top:115px;width:210px"><i class="chk">◎</i><p class="txt"><b>Complexity</b>: The project demanded a deep understanding of the unique financial aspects of the tech industry.</p></div>
  <div class="abs row" style="left:46px;top:170px;width:210px"><i class="chk">◎</i><p class="txt"><b>Impact</b>: The developed financial plan significantly shaped the client's business strategy and success.</p></div>
  <div class="abs row" style="left:46px;top:226px;width:210px"><i class="chk">▲</i><p class="txt"><b>Innovation</b>: Balancing aggressive growth with financial prudence required innovative thinking.</p></div>
  <div class="photo" style="left:278px;top:100px;width:230px;height:166px;border-radius:4px;background:linear-gradient(140deg,#2c2a86,#5a5ab4 60%,#8f8fcc)" role="img" aria-label="Chess pieces on a board, tinted navy"></div>
  <p class="abs" style="left:292px;top:236px;font-size:7px;line-height:1.3;color:#fff">Financial Blueprint for<br>Future Growth</p>
  <div class="pg">12</div>
</section>

<!-- 13 Blueprint bars -->
<section class="slide" style="left:61px;top:1958px">
  <div class="photo" style="left:36px;top:38px;width:300px;height:218px;border-radius:4px;background:linear-gradient(150deg,#6b6fa0,#3b3c8e 55%,#24227a)" role="img" aria-label="Colleagues working on laptops, tinted navy"></div>
  <h2 class="abs" style="left:52px;top:174px;font-size:14px;font-weight:500;line-height:1.15;color:#fff">Financial<br>Blueprint<br>for Future<br>Growth</h2>
  <p class="abs" style="left:150px;top:198px;width:170px;font-size:5.6px;line-height:1.45;color:#fff">This project involved the development of a comprehensive financial plan for a rapidly growing tech company. The plan was designed to support the company's ambitious growth objectives while ensuring financial stability and sustainability.</p>
  <div class="card" style="left:350px;top:38px;width:156px;height:66px;border-left:4px solid var(--navy);border-radius:0;padding:10px 12px"><p class="txt"><b>Complexity</b>: The project demanded a deep understanding of the unique financial aspects of the tech industry.</p></div>
  <div class="card" style="left:350px;top:114px;width:156px;height:66px;border-left:4px solid var(--gold);border-radius:0;padding:10px 12px"><p class="txt"><b>Impact</b>: The developed financial plan significantly shaped the client's business strategy and success.</p></div>
  <div class="card" style="left:350px;top:190px;width:156px;height:66px;border-left:4px solid var(--navy);border-radius:0;padding:10px 12px"><p class="txt"><b>Innovation</b>: Balancing aggressive growth with financial prudence required innovative thinking.</p></div>
  <div class="pg">13</div>
</section>

<!-- 14 Stages -->
<section class="slide" style="left:615px;top:1958px">
  <h2 class="ttl" style="left:36px;top:28px">Stages of <span class="gold">Financial</span> Planning</h2>
  <p class="abs txt" style="left:36px;top:62px;width:400px">Financial planning is a systematic process that helps organizations define and achieve their long-term financial goals. This process involves a series of key stages, each playing a crucial role in ensuring financial stability and growth.</p>
  <p class="abs" style="left:62px;top:94px;font-size:7px;font-weight:600">Key Stages:</p>
  <p class="abs" style="left:275px;top:94px;font-size:7px;font-weight:600">Key Performance Indicators (KPIs):</p>
  <div class="abs row" style="left:40px;top:112px;width:210px"><i class="chk">✓</i><p class="txt"><b>Goal Setting</b>: Defining clear, measurable, and achievable financial goals.</p></div>
  <div class="abs row" style="left:40px;top:135px;width:210px"><i class="chk">✓</i><p class="txt"><b>Data Gathering</b>: Collecting relevant financial information to understand the current financial status.</p></div>
  <div class="abs row" style="left:40px;top:158px;width:210px"><i class="chk">✓</i><p class="txt"><b>Analysis</b>: Evaluating the data to identify strengths, weaknesses, and opportunities.</p></div>
  <div class="abs row" style="left:40px;top:181px;width:210px"><i class="chk">✓</i><p class="txt"><b>Plan Development</b>: Creating a comprehensive financial plan based on the analysis.</p></div>
  <div class="abs row" style="left:40px;top:204px;width:210px"><i class="chk">✓</i><p class="txt"><b>Implementation</b>: Executing the financial plan while monitoring its progress.</p></div>
  <div class="abs row" style="left:40px;top:227px;width:210px"><i class="chk">✓</i><p class="txt"><b>Review and Update</b>: Regularly reviewing and updating the plan to reflect changes in financial goals or circumstances.</p></div>
  <div class="card" style="left:277px;top:114px;width:110px;height:62px;text-align:center;padding-top:14px;font-size:6px;font-weight:600;color:var(--navy)"><svg width="12" height="12" viewBox="0 0 12 12" style="display:block;margin:0 auto 5px"><rect x="1" y="1" width="10" height="10" fill="var(--navy)"/></svg>Budget<br>Adherence</div>
  <div class="card" style="left:397px;top:114px;width:110px;height:62px;text-align:center;padding-top:14px;font-size:6px;font-weight:600;color:var(--navy)"><svg width="12" height="12" viewBox="0 0 12 12" style="display:block;margin:0 auto 5px"><circle cx="6" cy="7" r="5" fill="var(--navy)"/></svg>Savings<br>Rate</div>
  <div class="card" style="left:277px;top:186px;width:110px;height:62px;text-align:center;padding-top:14px;font-size:6px;font-weight:600;color:var(--navy)"><svg width="12" height="12" viewBox="0 0 12 12" style="display:block;margin:0 auto 5px"><path d="M1 11V4l4 3 6-6v10z" fill="var(--navy)"/></svg>Debt-to-<br>Income Ratio</div>
  <div class="card" style="left:397px;top:186px;width:110px;height:62px;text-align:center;padding-top:14px;font-size:6px;font-weight:600;color:var(--navy)"><svg width="12" height="12" viewBox="0 0 12 12" style="display:block;margin:0 auto 5px"><rect x="1" y="3" width="10" height="7" rx="1" fill="var(--navy)"/></svg>Investment<br>Return</div>
  <div class="foot"><b>RT</b>Introduction to Ru Tambisk</div><div class="pg">14</div>
</section>

<!-- 15 Bubbles -->
<section class="slide" style="left:61px;top:2275px">
  <h2 class="ttl" style="left:36px;top:62px">Crafting a Successful<br><span class="gold">Investment Plan</span>:<br>Key Considerations</h2>
  <p class="abs txt" style="left:36px;top:148px;width:250px">Creating a robust investment plan begins with clearly defined investment goals that are specific, measurable, achievable, relevant, and time-bound. The next crucial step is understanding your risk tolerance, which will guide your asset allocation and diversification strategies. The length of time you plan to invest, known as your investment time horizon, also significantly influences your investment choices. It's important to consider your liquidity needs and the tax implications of your investments, as these can impact your overall returns. Costs associated with investments are another key consideration. Regular review and rebalancing of your investment plan ensure it continues to align with your goals. Lastly, while not directly controllable, understanding the current economic and market conditions can help inform your investment decisions.</p>
  <svg class="abs" style="left:0;top:0" width="542" height="304" viewBox="0 0 542 304" font-family="Poppins, sans-serif" text-anchor="middle">
    <g fill="#fff" stroke="#e4e4ea">
      <circle cx="267" cy="6" r="22"/><circle cx="326" cy="36" r="20"/><circle cx="386" cy="20" r="27"/><circle cx="447" cy="61" r="25"/><circle cx="490" cy="8" r="24"/>
      <circle cx="525" cy="108" r="20"/><circle cx="528" cy="175" r="26"/><circle cx="337" cy="263" r="27"/><circle cx="283" cy="285" r="20"/>
      <circle cx="444" cy="274" r="26"/><circle cx="498" cy="244" r="22"/><circle cx="508" cy="306" r="20"/><circle cx="321" cy="196" r="25"/>
    </g>
    <circle cx="373" cy="113" r="55" fill="var(--navy)"/>
    <circle cx="468" cy="122" r="31" fill="var(--lav)"/>
    <circle cx="438" cy="201" r="43" fill="var(--gold)"/>
    <g font-size="5" fill="var(--ink)" font-weight="600">
      <text x="267" y="4">Financial</text><text x="267" y="10">Advisor</text>
      <text x="326" y="34">Regular</text><text x="326" y="40">Review</text>
      <text x="386" y="22" font-size="7">Costs</text>
      <text x="447" y="59" font-size="6">Diversifi</text><text x="447" y="67" font-size="6">cation</text>
      <text x="490" y="4">Environment</text>
      <text x="525" y="105" font-size="6">Emergency</text><text x="525" y="113" font-size="6">Fund</text>
      <text x="528" y="173" font-size="6">Performance</text><text x="528" y="181" font-size="6">Measurement</text>
      <text x="337" y="260" font-size="6">Liquidity</text><text x="337" y="268" font-size="6">Needs</text>
      <text x="283" y="283">Exit</text><text x="283" y="289">Strategy</text>
      <text x="444" y="270" font-size="6">Tax</text><text x="444" y="278" font-size="6">Considera</text><text x="444" y="286" font-size="6">tions</text>
      <text x="498" y="241">Economic</text><text x="498" y="247">and Market</text><text x="498" y="253">Conditions</text>
      <text x="321" y="191" font-size="6">Investment</text><text x="321" y="199" font-size="6">Time</text><text x="321" y="207" font-size="6">Horizon</text>
    </g>
    <text x="373" y="111" font-size="9" fill="#fff">Investment</text><text x="373" y="122" font-size="9" fill="#fff">Goals</text>
    <text x="468" y="120" font-size="6.5" fill="#fff">Asset</text><text x="468" y="128" font-size="6.5" fill="#fff">Allocation</text>
    <text x="438" y="199" font-size="9" fill="#fff">Risk</text><text x="438" y="210" font-size="9" fill="#fff">Tolerance</text>
  </svg>
  <div class="foot"><b>RT</b>Introduction to Ru Tambisk</div>
</section>

<!-- 16 Six steps -->
<section class="slide" style="left:615px;top:2275px">
  <h2 class="ttl" style="left:36px;top:28px">Crafting an <span class="gold">Investment Strategy</span>:<br>A Six-Step Process</h2>
  <div class="step" style="left:36px;top:96px"><div class="no">01</div><p class="txt"><b>Identifying Investment Goals</b><br>This is the first step where you define what you want to achieve with your investments. These goals could be short-term or long-term, such as saving for a vacation, buying a house, or planning for retirement.</p></div>
  <div class="step" style="left:200px;top:96px"><div class="no">03</div><p class="txt"><b>Asset Allocation</b>: Based on your investment goals and risk tolerance, you decide how to distribute your investments among different asset classes. This could include a mix of stocks, bonds, real estate, and other investment types.</p></div>
  <div class="step" style="left:364px;top:96px"><div class="no">05</div><p class="txt"><b>Implementation</b>: This is where you actually make your investments. It's important to consider the timing of your investments and to diversify your portfolio to spread risk.</p></div>
  <div class="step" style="left:36px;top:190px"><div class="no">02</div><p class="txt"><b>Assessing Risk Tolerance</b>: This involves determining how much risk you are willing and able to take on. Your risk tolerance will influence the types of investments you make and how you allocate your assets.</p></div>
  <div class="step" style="left:200px;top:190px"><div class="no">04</div><p class="txt"><b>Investment Selection</b>: At this stage, you choose specific investments to include in your portfolio. This could involve selecting individual stocks or bonds, or using investment funds that track certain market indices.</p></div>
  <div class="step" style="left:364px;top:190px"><div class="no">06</div><p class="txt"><b>Monitoring and Adjusting</b>: Once your investment strategy is in place, it's important to regularly review your portfolio and make adjustments as needed. This could be due to changes in your financial situation, investment goals, or market conditions.</p></div>
  <div class="foot"><b>RT</b>Introduction to Ru Tambisk</div><div class="pg">16</div>
</section>

<!-- 17 Roadmap -->
<section class="slide" style="left:61px;top:2591px">
  <h2 class="ttl" style="left:36px;top:28px">Corporate <span class="gold">Investment Strategy</span>:<br>A Six-Step Roadmap</h2>
  <div class="rm" style="left:36px;top:100px"><div class="bd bg-navy">0–6<br>Months</div><p class="txt"><b>Capital Structure Optimization</b><br>Evaluate and adjust the mix of debt and equity to optimize the cost of capital.</p><i class="ring"></i></div>
  <div class="rm" style="left:274px;top:100px"><div class="bd bg-gold">3–5<br>Years</div><p class="txt"><b>Mergers and Acquisitions</b><br>Identify potential acquisition targets or merger partners to accelerate growth and increase market share.</p><i class="ring"></i></div>
  <div class="rm" style="left:36px;top:160px"><div class="bd bg-gold">6–12<br>Months</div><p class="txt"><b>Operational Efficiency Investments</b><br>Invest in technology or process improvements to increase operational efficiency and reduce costs.</p><i class="ring"></i></div>
  <div class="rm" style="left:274px;top:160px"><div class="bd bg-navy">5–10<br>Years</div><p class="txt"><b>Sustainability Investments</b><br>Invest in sustainable practices and technologies to enhance corporate social responsibility and long-term viability.</p><i class="ring"></i></div>
  <div class="rm" style="left:36px;top:220px"><div class="bd bg-navy">1–3<br>Years</div><p class="txt"><b>Market Expansion Initiatives</b><br>Allocate funds for market expansion activities such as new product development or geographic expansion.</p><i class="ring"></i></div>
  <div class="rm" style="left:274px;top:220px"><div class="bd bg-gold">Ongoing</div><p class="txt"><b>Performance Review and Adjustments</b><br>Continually assess investment performance and adjust as needed to align with corporate objectives and market trends.</p><i class="ring"></i></div>
  <div class="foot"><b>RT</b>Introduction to Ru Tambisk</div><div class="pg">17</div>
</section>

<!-- 18 Dashboard -->
<section class="slide" style="left:615px;top:2591px">
  <div class="tabs"><span class="on">Investment Overview</span><span>Performance Metrics</span><span>Risk Assessment</span><span>Investment Timeline</span><span>Financial Projections</span></div>
  <div class="card" style="left:36px;top:52px;width:140px;height:60px;padding:12px"><p style="font-size:15px;font-weight:600;color:var(--navy)">+570K <span style="font-size:7px;color:#aaa">▲</span></p><p class="txt" style="margin-top:3px">Lorem ipsum dolor sit amet</p></div>
  <div class="card" style="left:186px;top:52px;width:322px;height:60px;padding:12px 14px">
    <div class="abs" style="left:14px;top:16px;width:26px;height:26px;border-radius:50%;border:3px solid var(--navy);border-right-color:#ddd"></div>
    <div class="abs" style="right:8px;top:8px;width:20px;height:8px;border-radius:4px;background:var(--gold-soft)"></div>
    <p class="abs" style="left:50px;top:16px;font-size:7px;font-weight:600;color:var(--navy)"><span class="gold">Progress:</span> implementation of the plan</p>
    <p class="abs txt" style="left:50px;top:28px;width:250px">Lorem ipsum dolor sit amet, consectetur adipiscing elit, sed do eiusmod tempor incididunt ut labore et dolore magna aliqua. Ut enim ad minim veniam, quis nostrud</p>
  </div>
  <div class="card" style="left:36px;top:122px;width:140px;height:150px">
    <svg class="abs" style="left:18px;top:12px" width="104" height="104" viewBox="0 0 104 104" font-family="Poppins, sans-serif" font-size="5" text-anchor="middle" fill="#fff">
      <circle cx="52" cy="52" r="44" fill="var(--navy)"/><circle cx="52" cy="62" r="32" fill="var(--gold)"/><circle cx="52" cy="72" r="20" fill="var(--lav)"/>
      <text x="52" y="14">S1</text><text x="52" y="38">S2</text><text x="52" y="74">S3</text>
    </svg>
    <p class="abs" style="left:20px;top:122px;font-size:5px;line-height:1.6;color:var(--muted)">● Stage 1 &nbsp; ● Stage 2<br>&nbsp; ● Stage 3</p>
  </div>
  <div class="card" style="left:186px;top:122px;width:322px;height:150px">
    <p class="abs" style="left:14px;top:10px;font-size:7px;font-weight:600;color:var(--navy)">Description of current investment projects</p>
    <svg class="abs" style="left:12px;top:30px" width="300" height="110" viewBox="0 0 300 110" font-family="Poppins, sans-serif" font-size="5" fill="#999" text-anchor="middle">
      <g fill="#e4e4e8"><rect x="20" y="4" width="8" height="80" rx="4"/><rect x="70" y="4" width="8" height="80" rx="4"/><rect x="120" y="4" width="8" height="80" rx="4"/><rect x="170" y="4" width="8" height="80" rx="4"/><rect x="220" y="4" width="8" height="80" rx="4"/><rect x="270" y="4" width="8" height="80" rx="4"/></g>
      <rect x="20" y="48" width="8" height="36" rx="4" fill="var(--navy)"/><rect x="70" y="62" width="8" height="22" rx="4" fill="var(--gold)"/><rect x="120" y="40" width="8" height="44" rx="4" fill="var(--navy)"/><rect x="170" y="24" width="8" height="60" rx="4" fill="var(--gold)"/><rect x="220" y="30" width="8" height="54" rx="4" fill="var(--navy)"/><rect x="270" y="70" width="8" height="14" rx="4" fill="var(--gold)"/>
      <text x="24" y="98">Project</text><text x="74" y="98">Project</text><text x="124" y="98">Project</text><text x="174" y="98">Project</text><text x="224" y="98">Project</text><text x="274" y="98">Project</text>
    </svg>
  </div>
  <div class="foot"><b>RT</b>Introduction to Ru Tambisk</div><div class="pg">18</div>
</section>

<!-- 19 Metrics -->
<section class="slide" style="left:61px;top:2908px">
  <div class="tabs" style="top:36px;height:24px"><span>Investment Overview</span><span class="on">Performance Metrics</span><span>Risk Assessment</span><span>Investment Timeline</span><span>Financial Projections</span></div>
  <div class="card" style="left:36px;top:72px;width:222px;height:58px">
    <p class="abs" style="left:14px;top:12px;font-size:7px;font-weight:600;color:var(--navy)"><span style="color:#3c5bd8">Progress:</span> implementation of the plan</p>
    <p class="abs" style="left:14px;top:24px;width:194px;display:flex;justify-content:space-between;font-size:4px;color:#aaa"><span>0%</span><span>50%</span><span>100%</span></p>
    <div class="abs" style="left:14px;top:32px;width:194px;height:9px;border-radius:5px;background:#e4e4ea"><div style="width:66%;height:100%;border-radius:5px;background:var(--navy)"></div></div>
  </div>
  <div class="abs bg-gold" style="left:268px;top:72px;width:84px;height:58px;border-radius:4px;color:#fff;font-size:15px;font-weight:600;display:flex;align-items:center;justify-content:center">+570K ▴</div>
  <p class="abs txt" style="left:362px;top:78px;width:140px">Lorem ipsum dolor sit amet, consectetur adipiscing elit, sed do eiusmod tempor incididunt ut labore et dolore magna aliqua. Ut enim ad minim veniam, quis nostrud</p>
  <div class="card" style="left:36px;top:140px;width:108px;height:132px">
    <svg class="abs" style="left:26px;top:12px" width="60" height="60" viewBox="0 0 60 60" font-family="Poppins, sans-serif" text-anchor="middle">
      <circle cx="30" cy="32" r="24" fill="none" stroke="#e4e4ea" stroke-width="4"/><path d="M30 8a24 24 0 1 1-22 33" fill="none" stroke="var(--navy)" stroke-width="4"/><path d="M8 41A24 24 0 0 1 22 10" fill="none" stroke="var(--gold)" stroke-width="4"/>
      <text x="30" y="30" font-size="8" font-weight="600" fill="var(--ink)">20YY</text><text x="30" y="37" font-size="4" fill="#888">Lorem</text><text x="30" y="42" font-size="4" fill="#888">ipsum dolor</text>
      <circle cx="51" cy="11" r="6" fill="#fff" stroke="#3c5bd8"/><path d="M48 11l2 2 4-4" stroke="#3c5bd8" fill="none"/>
    </svg>
    <p class="abs" style="left:0;right:0;top:90px;text-align:center;font-size:6px;font-weight:600">Description</p>
    <p class="abs txt" style="left:14px;right:14px;top:100px;text-align:center">Lorem ipsum dolor sit amet, consectetur</p>
  </div>
  <div class="card" style="left:152px;top:140px;width:108px;height:132px">
    <svg class="abs" style="left:26px;top:12px" width="60" height="60" viewBox="0 0 60 60" font-family="Poppins, sans-serif" text-anchor="middle">
      <circle cx="30" cy="32" r="24" fill="none" stroke="#e4e4ea" stroke-width="4"/><path d="M30 8a24 24 0 1 1-24 24" fill="none" stroke="var(--navy)" stroke-width="4"/><path d="M6 32A24 24 0 0 1 18 11" fill="none" stroke="var(--gold)" stroke-width="4"/>
      <text x="30" y="30" font-size="8" font-weight="600" fill="var(--ink)">20YY</text><text x="30" y="37" font-size="4" fill="#888">Lorem</text><text x="30" y="42" font-size="4" fill="#888">ipsum dolor</text>
      <circle cx="51" cy="11" r="6" fill="#fff" stroke="#3c5bd8"/><path d="M48 11l2 2 4-4" stroke="#3c5bd8" fill="none"/>
    </svg>
    <p class="abs" style="left:0;right:0;top:90px;text-align:center;font-size:6px;font-weight:600">Description</p>
    <p class="abs txt" style="left:14px;right:14px;top:100px;text-align:center">Lorem ipsum dolor sit amet, consectetur</p>
  </div>
  <div class="card" style="left:268px;top:140px;width:240px;height:132px">
    <p class="abs" style="left:12px;top:10px;font-size:7px;font-weight:600;color:var(--navy)"><span style="color:#3c5bd8">Progress:</span> implementation of the plan</p>
    <svg class="abs" style="left:8px;top:26px" width="226" height="100" viewBox="0 0 226 100" font-family="Poppins, sans-serif" font-size="4.5" fill="#999">
      <g stroke="#eee"><line x1="18" y1="8" x2="222" y2="8"/><line x1="18" y1="28" x2="222" y2="28"/><line x1="18" y1="48" x2="222" y2="48"/><line x1="18" y1="68" x2="222" y2="68"/><line x1="18" y1="86" x2="222" y2="86"/></g>
      <text x="2" y="10">200</text><text x="2" y="30">120</text><text x="2" y="50">80</text><text x="2" y="70">15</text><text x="2" y="88">0</text>
      <g fill="var(--navy)"><rect x="34" y="58" width="4" height="28"/><rect x="70" y="50" width="4" height="36"/><rect x="106" y="44" width="4" height="42"/><rect x="142" y="24" width="4" height="62"/><rect x="178" y="36" width="4" height="50"/></g>
      <g fill="var(--gold)"><rect x="40" y="66" width="4" height="20"/><rect x="76" y="62" width="4" height="24"/><rect x="112" y="58" width="4" height="28"/><rect x="148" y="40" width="4" height="46"/><rect x="184" y="52" width="4" height="34"/></g>
      <g fill="#b9c4ee"><rect x="46" y="72" width="4" height="14"/><rect x="82" y="70" width="4" height="16"/><rect x="118" y="66" width="4" height="20"/><rect x="154" y="60" width="4" height="26"/><rect x="190" y="64" width="4" height="22"/></g>
      <text x="36" y="96">April</text><text x="73" y="96">May</text><text x="108" y="96">June</text><text x="145" y="96">July</text><text x="178" y="96">August</text>
    </svg>
  </div>
  <div class="foot"><b>RT</b>Introduction to Ru Tambisk</div><div class="pg">19</div>
</section>

</body>
</html>
```